business card for training & coaching company, Brightwell.co

Create a warm, clean, professional 2-sided business card for Brightwell.co.
Brightwell.co is a new company that shares Brightwell Dialogue (combination of mindfulness, kindness, and nonviolent communication), training and coaching individuals and groups.
Include the logo provided, perhaps incorporating a second opaque version of it as well.
Feelings & Needs lists on the reverse side of the card.

Target Market(s)

Women 30-60 years old, university educated.
Spiritual, may be Buddhist.

Industry/Entity Type

Training

Contact Information for Business Card

Jessamine T. Holloway, MSc
Group Facilitator & Certified Wellness Coach
Brightwell Dialogue training & support
Group Facilitator & Coach
01482 936 555
07754 608 219
www.brightwell.co

Font styles to use
Sans Serif

Requirements
Must have
• Front -- Contact details, logo provided.
• Back -- Feelings list; Needs list
• Professional yet warm, inviting, friendly feel.
Nice to have
• little graphics (telephone for phone number, envelope for email, globe for web);
• Clean font (like Sathu, Frutiga, Helvetica).
• Feeling of movement or transformation.
Should not have
• More than 3 colours.
• Loud or busy designs.
• A gentle curve or two is ok, but not swirly designs.
• No black or other heavy backgrounds.

```html
<!DOCTYPE html>
<html lang="en">
<head>
<meta charset="utf-8">
<title>Brightwell.co business card</title>
<link rel="stylesheet" href="https://fonts.googleapis.com/css2?family=Arimo:wght@400;600&display=swap">
<style>
  :root {
    --orange-light: #f7941d;
    --orange-deep: #f15a24;
    --orange-text: #e8552a;
    --ink: #3a3a3a;
    --peach: #fbd9c4;
    --white: #ffffff;
    --stage: #ececec;
  }
  * { margin: 0; padding: 0; box-sizing: border-box; }
  html, body {
    width: 1200px; height: 1008px; overflow: hidden;
    background: var(--stage);
    font-family: "Arimo", Arial, Helvetica, sans-serif;
  }
  .canvas { position: relative; width: 1200px; height: 1008px; }
  .card {
    position: absolute; width: 760px; height: 435px; overflow: hidden;
    box-shadow: 0 4px 14px rgba(0,0,0,0.15);
  }
  .card-front {
    left: 68px; top: 45px;
    background: radial-gradient(ellipse at 50% 55%, var(--white) 30%, var(--peach) 100%);
  }
  .card-back { left: 345px; top: 526px; background: var(--white); }
  .band { position: absolute; left: 0; top: 0; width: 760px; height: 435px; }
  .centered { position: absolute; left: 0; width: 100%; text-align: center; }

  .role-title { top: 30px; font-size: 21px; color: var(--ink); }
  .brand-mark {
    top: 108px; display: flex; justify-content: center; align-items: center; gap: 10px;
    font-size: 28px; font-weight: 600; color: var(--orange-deep);
  }
  .brand-dot { width: 16px; height: 16px; border-radius: 50%; background: var(--orange-light); }
  .person-name { top: 232px; font-size: 30px; color: var(--white); }
  .person-credentials { top: 273px; font-size: 21px; color: var(--white); }
  .phones { top: 353px; font-size: 27px; color: var(--orange-text); }
  .website { top: 390px; font-size: 20px; letter-spacing: 9px; color: var(--orange-text); }

  .tagline { top: 27px; font-size: 23px; color: var(--white); }
  .list-heading { font-size: 26px; color: var(--orange-text); }
  .feelings-heading { top: 131px; }
  .needs-heading { top: 255px; }
  .word-list { font-size: 19px; line-height: 26px; color: var(--ink); }
  .feelings-list { top: 170px; }
  .needs-list { top: 292px; }
  .divider {
    position: absolute; left: 112px; top: 239px; width: 536px;
    border-top: 2px dotted #b5b5b5;
  }
</style>
</head>
<body>
<div class="canvas">
  <section class="card card-front">
    <svg class="band" viewBox="0 0 760 435" aria-hidden="true">
      <defs>
        <linearGradient id="frontBand" x1="0" y1="0" x2="1" y2="1">
          <stop offset="0" stop-color="#f7941d"/>
          <stop offset="1" stop-color="#f15a24"/>
        </linearGradient>
      </defs>
      <path d="M0,157 C250,230 500,200 760,145 L760,365 C520,300 250,330 0,365 Z" fill="url(#frontBand)"/>
    </svg>
    <p class="centered role-title">GROUP FACILITATOR &amp; CERTIFIED WELLNESS COACH</p>
    <div class="centered brand-mark"><span class="brand-dot"></span><span>Brightwell.co</span></div>
    <h1 class="centered person-name" style="font-weight:400">Jessamine T. Holloway</h1>
    <p class="centered person-credentials">MSc &amp; Certified Wellness Coach Group Facilitator &amp; Coach</p>
    <p class="centered phones">01482 936 555 / 07754 608 219</p>
    <p class="centered website">www.brightwell.co</p>
  </section>

  <section class="card card-back">
    <svg class="band" viewBox="0 0 760 435" aria-hidden="true">
      <defs>
        <linearGradient id="backBand" x1="0" y1="0" x2="1" y2="1">
          <stop offset="0" stop-color="#f7941d"/>
          <stop offset="1" stop-color="#f15a24"/>
        </linearGradient>
      </defs>
      <path d="M0,0 H760 V52 C600,110 300,130 0,55 Z" fill="url(#backBand)"/>
      <path d="M0,409 C200,370 400,355 520,358 C620,360 700,365 760,376 V435 H0 Z" fill="url(#backBand)"/>
    </svg>
    <p class="centered tagline">Brightwell Dialogue training &amp; support</p>
    <h2 class="centered list-heading feelings-heading" style="font-weight:400">FEELINGS</h2>
    <p class="centered word-list feelings-list">Confusion &nbsp;|&nbsp; Curious &nbsp;|&nbsp; Despair &nbsp;|&nbsp; Edgy &nbsp;|&nbsp; Fiery &nbsp;|&nbsp; Grief &nbsp;|&nbsp; Nervous<br>Powerless &nbsp;|&nbsp; Shock &nbsp;|&nbsp; Torn &nbsp;|&nbsp; Weary &amp; more...</p>
    <div class="divider"></div>
    <h2 class="centered list-heading needs-heading" style="font-weight:400">NEEDS</h2>
    <p class="centered word-list needs-list">Belonging &nbsp;|&nbsp; Choice &nbsp;|&nbsp; Clarity &nbsp;|&nbsp; Empathy &nbsp;|&nbsp; Freedom &nbsp;|&nbsp; Meaning<br>Mourning &nbsp;|&nbsp; Peace &nbsp;|&nbsp; Safety &nbsp;|&nbsp; Support &nbsp;|&nbsp; Understanding &amp; more...</p>
  </section>
</div>
</body>
</html>
```